Change an Existing THEME on a Shopify Site

We currently have a Shopify Site that we would like to launch soon. We picked a current theme [Tavel] and have made some basic changes to it but we don't really know what we're doing. We would like a new theme based on this one specifically built for our site. We already brand colours and a logo.

```html
<!DOCTYPE html>
<html lang="en">
<head>
<meta charset="utf-8">
<title>Maple Paws — Home</title>
<link href="https://fonts.googleapis.com/css2?family=Roboto+Condensed:wght@500;600;700&family=Roboto:wght@400;500;700&display=swap" rel="stylesheet">
<style>
:root{
  --navy:#121a45;
  --mint:#a9e7e0;
  --mint-pale:#e2fbf8;
  --orange:#f59b3a;
  --coral:#fd6a3b;
  --teal:#1a6f6b;
  --white:#ffffff;
  --ink:#1b1f2e;
  --muted:#6b6f7c;
}
*{box-sizing:border-box;margin:0;padding:0}
html,body{width:1200px;height:4612px;overflow:hidden}
body{background:var(--navy);font-family:"Roboto",sans-serif;color:var(--ink)}
.page{position:relative;width:1200px;height:4612px;overflow:hidden;background:var(--navy)}
.abs{position:absolute}
.head{font-family:"Roboto Condensed",sans-serif;font-weight:600}
svg{display:block}

.nav a{position:absolute;top:26px;color:var(--white);font:500 15px "Roboto",sans-serif;text-decoration:none}
.nav .active::before{content:"";position:absolute;left:0;right:0;top:-26px;height:4px;background:var(--white)}
.icon-btn{position:absolute;top:24px}
.cart-count{position:absolute;left:1036px;top:19px;width:17px;height:17px;border-radius:50%;background:var(--white);color:var(--navy);font:700 10px "Roboto",sans-serif;text-align:center;line-height:17px}

.brand{position:absolute;left:132px;top:2px;width:158px;height:158px;border-radius:50%;background:var(--mint);border:6px solid var(--navy);display:flex;align-items:center;justify-content:center;color:var(--navy);font:700 22px "Roboto Condensed",sans-serif;text-align:center;line-height:1.05;z-index:3}

.hero-kicker{left:152px;top:284px;color:var(--navy);font:500 20px "Roboto",sans-serif}
.hero-title{left:152px;top:308px;color:var(--navy);font:500 48px/48px "Roboto",sans-serif}
.dot-btn{position:absolute;width:36px;height:36px;border-radius:50%;display:flex;align-items:center;justify-content:center}
.placeholder{position:absolute}

.section-title{position:absolute;left:0;width:1200px;text-align:center;color:var(--white);font-size:31px}
.kicker{position:absolute;left:0;width:1200px;text-align:center;color:var(--teal);font-size:18px}
.rule{position:absolute;left:575px;width:50px;height:3px;background:var(--teal)}
.chev{position:absolute;width:20px;height:28px}

.cat{position:absolute;top:752px;width:186px;text-align:center}
.cat-circle{width:186px;height:186px;border-radius:50%;background:var(--white);position:relative}
.cat-art{position:absolute;left:38px;top:38px;width:110px;height:110px;border-radius:50%}
.cat-name{margin-top:18px;color:var(--white);font:500 19px "Roboto",sans-serif}

.about-photo{position:absolute;border:2px solid var(--navy);border-radius:8px}
.about-text{left:625px;width:425px}
.about-body{position:absolute;left:625px;top:1282px;width:425px;font-size:14.5px;line-height:24px;color:#444a5a;text-align:justify}
.btn{position:absolute;background:var(--orange);color:var(--white);font:700 14px "Roboto",sans-serif;border-radius:4px;display:flex;align-items:center;justify-content:center;letter-spacing:.3px}

.band{left:0;top:1741px;width:1200px;height:54px;background:var(--navy)}
.band span{position:absolute;top:10px;color:var(--white);font:700 30px "Roboto Condensed",sans-serif}

.product{position:absolute;top:1988px;width:287px;height:435px;background:#c4f0ea;border-radius:6px}
.product.featured{background:var(--white);border:3px solid var(--teal);border-radius:8px}
.product-img{position:absolute;left:20px;top:20px;right:20px;height:244px;background:var(--white);border-radius:4px}
.product-art{position:absolute;left:40px;right:40px;top:40px;bottom:40px;border-radius:50% 50% 40% 40%}
.product-name{position:absolute;top:284px;left:0;right:0;text-align:center;font:600 19px "Roboto Condensed",sans-serif;color:var(--ink)}
.price{position:absolute;top:316px;left:0;right:0;text-align:center;font:400 19px "Roboto Condensed",sans-serif;color:var(--ink)}
.price s{color:var(--muted);margin-right:8px}
.product .btn{left:54px;top:358px;width:179px;height:47px}
.product.featured .btn{left:51px;top:355px}

.review{position:absolute;top:2778px;width:287px;height:222px;background:var(--white);border-radius:4px;text-align:center}
.review.featured{border:7px solid #7fd3cd;border-radius:6px}
.stars{margin-top:34px;color:var(--orange);font-size:17px;letter-spacing:5px}
.review p{margin:10px auto 0;width:240px;font-size:14px;line-height:24px;color:#6b6f7c}
.review .who{margin-top:16px;font-size:14.5px;color:var(--ink)}
.review .who b{font-weight:700}

.promo{position:absolute;width:457px;height:401px}
.promo h3{position:absolute;left:58px;top:72px;width:370px;color:var(--white);font:500 34px/48px "Roboto",sans-serif}
.promo p{position:absolute;left:58px;top:232px;width:340px;color:#fff6ea;font-size:12.5px;line-height:24px}

.foot-h{position:absolute;top:4273px;color:var(--white);font-size:23px}
.email{position:absolute;left:143px;top:4325px;width:341px;height:41px;background:var(--white);border-radius:6px;border-left:4px solid var(--orange);color:#777;font-size:12px;padding:13px 14px}
.links{position:absolute;left:582px;top:4322px;list-style:none}
.links li{color:var(--white);font-size:15px;height:24px;line-height:24px;padding-left:32px;position:relative}
.links li::before{content:"»";position:absolute;left:0;color:var(--orange);font-size:15px}
.contact{position:absolute;left:874px;color:var(--white);font-size:15px;line-height:22px;width:300px}
.contact .hot{color:var(--orange);font-size:20px;font-weight:500;margin-top:2px}
.ci{position:absolute;left:842px}
.pay{position:absolute;top:4562px;width:38px;height:22px;border-radius:3px}
.copy{position:absolute;left:700px;top:4563px;width:357px;text-align:right;color:var(--white);font-size:14.5px}
</style>
</head>
<body>
<div class="page">

  <svg class="abs" style="left:0;top:0" width="1200" height="660" aria-hidden="true">
    <path d="M56 112 Q56 73 95 73 H1105 Q1144 73 1144 112 V592 Q1000 585 820 600 Q560 625 400 642 Q200 660 56 618 Z" fill="var(--mint)"/>
  </svg>

  <div class="brand">Maple<br>Paws</div>

  <nav class="nav">
    <a class="active" style="left:451px" href="#">Home</a>
    <a style="left:537px" href="#">Shop</a>
    <a style="left:618px" href="#">About us</a>
    <a style="left:726px" href="#">Help</a>
    <a style="left:803px" href="#">Blog</a>
  </nav>
  <svg class="icon-btn" style="left:914px" width="22" height="22" viewBox="0 0 22 22" aria-label="Search"><circle cx="9" cy="9" r="7" fill="none" stroke="#fff" stroke-width="2"/><line x1="14" y1="14" x2="20" y2="20" stroke="#fff" stroke-width="2"/></svg>
  <svg class="icon-btn" style="left:966px" width="22" height="22" viewBox="0 0 22 22" aria-label="Account"><circle cx="11" cy="7" r="5" fill="none" stroke="#fff" stroke-width="2"/><path d="M2 21 Q11 10 20 21" fill="none" stroke="#fff" stroke-width="2"/></svg>
  <svg class="icon-btn" style="left:1020px" width="22" height="22" viewBox="0 0 22 22" aria-label="Cart"><rect x="3" y="7" width="16" height="13" rx="2" fill="none" stroke="#fff" stroke-width="2"/><path d="M7 7 V5 Q11 0 15 5 V7" fill="none" stroke="#fff" stroke-width="2"/></svg>
  <div class="cart-count">0</div>

  <div class="abs hero-kicker">WELCOME TO</div>
  <h1 class="abs hero-title">MAPLE<br>PAWS</h1>
  <div class="dot-btn" style="left:156px;top:473px;background:var(--white)"><svg width="10" height="14"><path d="M8 2 L3 7 L8 12" fill="none" stroke="#555" stroke-width="2"/></svg></div>
  <div class="dot-btn" style="left:204px;top:473px;background:var(--orange)"><svg width="10" height="14"><path d="M2 2 L7 7 L2 12" fill="none" stroke="#fff" stroke-width="2"/></svg></div>

  <div class="placeholder" role="img" aria-label="Illustration of three cartoon puppies" style="left:421px;top:90px;width:707px;height:447px;border-radius:45% 45% 30% 30%;background:radial-gradient(ellipse at 60% 55%,#f4a24a 0%,#e8a867 40%,rgba(169,231,224,0) 72%)"></div>

  <h2 class="section-title head" style="top:688px">SHOP BY CATEGORIES</h2>
  <svg class="chev" style="left:60px;top:831px" viewBox="0 0 20 28" aria-label="Previous"><path d="M15 4 L6 14 L15 24" fill="none" stroke="#fff" stroke-width="3"/></svg>
  <svg class="chev" style="left:1118px;top:831px" viewBox="0 0 20 28" aria-label="Next"><path d="M5 4 L14 14 L5 24" fill="none" stroke="#fff" stroke-width="3"/></svg>
  <div class="cat" style="left:152px"><div class="cat-circle"><div class="cat-art" role="img" aria-label="Puppy baking illustration" style="background:radial-gradient(circle,#f2a04c,#f7e7d6 70%,#fff)"></div></div><div class="cat-name">Cook and Bake</div></div>
  <div class="cat" style="left:383px"><div class="cat-circle"><div class="cat-art" role="img" aria-label="Sitting puppy illustration" style="background:radial-gradient(circle,#ee9a45,#f7e7d6 70%,#fff)"></div></div><div class="cat-name">Keep and Store</div></div>
  <div class="cat" style="left:616px"><div class="cat-circle"><div class="cat-art" role="img" aria-label="Lying puppy illustration" style="background:radial-gradient(circle,#6b4a3a,#e9ddd4 70%,#fff)"></div></div><div class="cat-name">Kids and Toys</div></div>
  <div class="cat" style="left:847px"><div class="cat-circle"><div class="cat-art" role="img" aria-label="Playful puppy illustration" style="background:radial-gradient(circle,#f0a048,#f7e7d6 70%,#fff)"></div></div><div class="cat-name">Lunch and Drink</div></div>

  <svg class="abs" style="left:0;top:1030px" width="1200" height="711" aria-hidden="true">
    <path d="M0 40 Q150 0 300 28 T600 30 T900 28 T1200 18 V711 H0 Z" fill="var(--mint-pale)"/>
  </svg>
  <div class="about-photo" role="img" aria-label="Photo of food containers being placed in a fridge" style="left:143px;top:1264px;width:221px;height:376px;background:linear-gradient(160deg,#7d8a8c,#d9dcd6 45%,#8fa073 80%,#5d6d55)"></div>
  <div class="about-photo" role="img" aria-label="Photo of a woman holding storage containers" style="left:378px;top:1184px;width:220px;height:376px;background:linear-gradient(170deg,#f4a9c4,#f6bfd2 50%,#e46274)"></div>
  <div class="abs head about-text" style="top:1180px;color:var(--teal);font-size:18px">WELCOME TO</div>
  <h2 class="abs about-text" style="top:1206px;color:var(--ink);font:500 41px 'Roboto',sans-serif">LUMORA</h2>
  <div class="abs" style="left:625px;top:1264px;width:52px;height:3px;background:var(--teal)"></div>
  <p class="about-body">Lorem ipsum dolor sit amet, consectetur adipiscing elit, sed do eiusmod tempor incididunt ut labore et dolore magna aliqua. Ut enim ad minim veniam, quis nostrud exercitation ullamco laboris nisi ut aliquip ex ea commodo consequat. Duis aute irure dolor in reprehenderit in voluptate velit esse cillum dolore eu fugiat nulla pariatur. Excepteur sint occaecat cupidatat non proident, sunt in culpa qui officia deserunt mollit anim id est laborum. Lorem ipsum dolor sit amet, consectetur adipiscing elit, sed do eiusmod tempor incididunt ut labore et dolore magna aliqua. Ut enim ad minim veniam, quis nostrud exercitation ullamco laboris nisi ut aliquip ex ea commodo consequat.</p>
  <div class="btn" style="left:625px;top:1590px;width:179px;height:47px">DISCOVER MORE</div>

  <div class="abs band"><span style="left:25px">BOXWELL</span><span style="left:539px">BOXWELL</span><span style="left:1004px">BOXWELL</span></div>

  <div class="abs" style="left:0;top:1795px;width:1200px;height:760px;background:var(--mint-pale)"></div>
  <svg class="abs" style="left:0;top:2508px" width="1200" height="60" aria-hidden="true">
    <path d="M0 26 Q150 0 300 22 T600 26 T900 22 T1200 28 V60 H0 Z" fill="var(--navy)"/>
  </svg>
  <div class="kicker head" style="top:1870px">OUR PRODUCTS</div>
  <h2 class="section-title" style="top:1899px;color:var(--ink);font:500 40px 'Roboto',sans-serif">FEATURED PRODUCTS</h2>
  <div class="rule" style="top:1956px"></div>
  <svg class="chev" style="left:60px;top:2193px" viewBox="0 0 20 28" aria-label="Previous"><path d="M15 4 L6 14 L15 24" fill="none" stroke="#222" stroke-width="3"/></svg>
  <svg class="chev" style="left:1118px;top:2193px" viewBox="0 0 20 28" aria-label="Next"><path d="M5 4 L14 14 L5 24" fill="none" stroke="#222" stroke-width="3"/></svg>

  <div class="product" style="left:143px"><div class="product-img"><div class="product-art" role="img" aria-label="Photo of colourful round storage bowls" style="background:linear-gradient(135deg,#ff8a1e,#ff3c8e 40%,#b7f02a 60%,#1a73e8)"></div></div><div class="product-name">PRODUCT 1</div><div class="price"><s>$50.00</s>$25.00</div><div class="btn">ADD TO CART</div></div>
  <div class="product featured" style="left:455px;width:290px"><div class="product-img"><div class="product-art" role="img" aria-label="Photo of a stack of colourful bowls" style="left:70px;right:70px;background:linear-gradient(180deg,#ff2f8a,#1a73e8 35%,#ff8a1e 60%,#c9f02a)"></div></div><div class="product-name">PRODUCT 2</div><div class="price"><s>$50.00</s>$25.00</div><div class="btn">ADD TO CART</div></div>
  <div class="product" style="left:770px"><div class="product-img"><div class="product-art" role="img" aria-label="Photo of a pink round storage bowl" style="top:80px;bottom:70px;background:linear-gradient(180deg,#f9a6d0,#e0479a)"></div></div><div class="product-name">PRODUCT 3</div><div class="price"><s>$50.00</s>$25.00</div><div class="btn">ADD TO CART</div></div>

  <div class="abs head" style="left:0;top:2655px;width:1200px;text-align:center;color:var(--white);font-size:18px">REVIEWS</div>
  <h2 class="section-title" style="top:2683px;font:500 40px 'Roboto',sans-serif">TESTIMONIALS</h2>
  <div class="rule" style="top:2738px;background:var(--white)"></div>
  <svg class="chev" style="left:60px;top:2878px" viewBox="0 0 20 28" aria-label="Previous"><path d="M15 4 L6 14 L15 24" fill="none" stroke="#fff" stroke-width="3"/></svg>
  <svg class="chev" style="left:1118px;top:2878px" viewBox="0 0 20 28" aria-label="Next"><path d="M5 4 L14 14 L5 24" fill="none" stroke="#fff" stroke-width="3"/></svg>
  <div class="review" style="left:143px"><div class="stars">★★★★★</div><p>Lorem ipsum dolor sit amet, consec tetur adipiscing elit, sed do eiusmod tempor incididunt ut labore et dolore magna aliqua.</p><div class="who"><b>John Doe</b> &nbsp;-&nbsp; Company name</div></div>
  <div class="review featured" style="left:446px;width:308px;top:2772px;height:236px"><div class="stars">★★★★★</div><p>Lorem ipsum dolor sit amet, consec tetur adipiscing elit, sed do eiusmod tempor incididunt ut labore et dolore magna aliqua.</p><div class="who"><b>John Doe</b> &nbsp;-&nbsp; Company name</div></div>
  <div class="review" style="left:770px"><div class="stars">★★★★★</div><p>Lorem ipsum dolor sit amet, consec tetur adipiscing elit, sed do eiusmod tempor incididunt ut labore et dolore magna aliqua.</p><div class="who"><b>John Doe</b> &nbsp;-&nbsp; Company name</div></div>
  <div class="abs" style="left:596px;top:3005px;width:9px;height:9px;border-radius:50%;background:var(--white)"></div>

  <div class="abs" style="left:0;top:3125px;width:1200px;height:1060px;background:var(--mint-pale)"></div>
  <svg class="abs" style="left:0;top:4150px" width="1200" height="60" aria-hidden="true">
    <path d="M0 26 Q150 0 300 22 T600 26 T900 22 T1200 28 V60 H0 Z" fill="var(--navy)"/>
  </svg>
  <div class="promo" style="left:143px;top:3238px;background:var(--orange)"><h3>LOREM IPSUM DOLOR SIT AMET, CONSEC TETUR ADIPISCING</h3><p>Lorem ipsum dolor sit amet, consectetur adipiscing elit, sed do eiusmod tempor incididunt ut labore et dolore magna aliqua. Ut enim ad minim veniam, quis nostrud exercitation ullamco laboris nisi ut</p></div>
  <div class="promo" role="img" aria-label="Photo of prepared meals in clear containers on a counter" style="left:600px;top:3238px;background:linear-gradient(160deg,#3a3f44,#b4bcc2 35%,#a9552f 55%,#5d7a3a 75%,#1e2226)"></div>
  <div class="promo" role="img" aria-label="Photo of hands holding stacked containers of vegetables" style="left:143px;top:3639px;background:linear-gradient(170deg,#7a9a86,#b7c9bb 45%,#d9e4dc 60%,#f08a3a 85%,#6d7c6f)"></div>
  <div class="promo" style="left:600px;top:3639px;background:var(--coral)"><h3>LOREM IPSUM DOLOR SIT AMET, CONSEC TETUR ADIPISCING</h3><p>Lorem ipsum dolor sit amet, consectetur adipiscing elit, sed do eiusmod tempor incididunt ut labore et dolore magna aliqua. Ut enim ad minim veniam, quis nostrud exercitation ullamco laboris nisi ut</p></div>

  <h3 class="foot-h head" style="left:143px">SUBSCRIBE TO OUR NEWSLETTER</h3>
  <h3 class="foot-h head" style="left:582px">MY ACCOUNT</h3>
  <h3 class="foot-h head" style="left:842px">CONTACT US</h3>
  <div class="email">Email address</div>
  <div class="btn" style="left:148px;top:4379px;width:336px;height:41px;font-size:12px">SUBSCRIBE</div>
  <div class="abs" style="left:309px;top:4443px;width:16px;height:16px;border-radius:50%;background:var(--white)"></div>
  <ul class="links">
    <li>About us</li><li>Contact</li><li>Faq</li><li>Privacy policy</li><li>Return and exchange</li><li>Shipping policy</li><li>Terms &amp; condition</li>
  </ul>
  <svg class="ci" style="top:4325px" width="16" height="16" viewBox="0 0 16 16" aria-label="Phone"><path d="M3 1 L6 1 L7 5 L5 6 Q6 9 10 11 L11 9 L15 10 L15 13 Q14 15 12 15 Q2 13 1 3 Q1 1 3 1Z" fill="var(--orange)"/></svg>
  <div class="contact" style="top:4322px">Hotline free 24/7<div class="hot">0400 123 456</div></div>
  <svg class="ci" style="top:4398px" width="16" height="13" viewBox="0 0 16 13" aria-label="Email"><rect width="16" height="13" rx="1" fill="var(--orange)"/><path d="M1 1 L8 7 L15 1" fill="none" stroke="var(--navy)" stroke-width="1.5"/></svg>
  <div class="contact" style="top:4392px">hello@maplepaws.com</div>
  <svg class="ci" style="top:4443px" width="14" height="18" viewBox="0 0 14 18" aria-label="Address"><path d="M7 18 Q0 9 0 7 A7 7 0 0 1 14 7 Q14 9 7 18Z" fill="var(--orange)"/><circle cx="7" cy="7" r="2.5" fill="var(--navy)"/></svg>
  <div class="contact" style="top:4440px">12 Sample Lane, Brookvale Heights<br>QLD 4000, Australia</div>

  <div class="pay" style="left:147px;background:#2d6fd6"></div>
  <div class="pay" style="left:194px;background:#f2f2f2"></div>
  <div class="pay" style="left:241px;background:#f2f2f2"></div>
  <div class="pay" style="left:288px;background:#f2f2f2"></div>
  <div class="pay" style="left:335px;background:#f2f2f2"></div>
  <div class="pay" style="left:382px;background:#5a31f4"></div>
  <div class="pay" style="left:429px;background:#1f7f8c"></div>
  <div class="pay" style="left:476px;background:#f2f2f2"></div>
  <div class="copy">© &nbsp;Copyrights 2025 | All Rights Reserved</div>
</div>
</body>
</html>
```